Litigation Support Company Needing new Simple Web Design

I need to re-design a self done wix hosted website for a small yet nation-wide litigation support consulting firm. I built mine at www.brieflantern-hub.com myself when I launched but it is very hard on the eyes and needs refreshing/updates. Thanks for taking a look!

Target Market(s)

Law firms and technology experts in the litigation support field.

Number of Pages Required

4 page

Font styles to use
Serif

Colors
f78f20
faa54b
fac994

Requirements
Must have
• Blog, About Us, Services Pages, Crisper Graphics etc.

```html
<!DOCTYPE html>
<html lang="en">
<head>
<meta charset="utf-8">
<title>brieflantern — Litigation Support</title>
<link rel="stylesheet" href="https://fonts.googleapis.com/css2?family=Poppins:wght@300;400;500;600;700&display=swap">
<style>
:root{
  --orange:#f78f20;
  --orange-mid:#faa54b;
  --orange-soft:#fac994;
  --ink:#222222;
  --text:#3a3a3a;
  --muted:#777777;
  --dark:#1c1512;
  --footer:#141414;
  --white:#ffffff;
}
*{box-sizing:border-box;margin:0;padding:0}
html,body{width:1200px;height:2970px;overflow:hidden}
body{position:relative;font-family:'Poppins',sans-serif;color:var(--text);background:var(--white)}
.abs{position:absolute}

/* hero */
.hero{left:0;top:0;width:1200px;height:760px;background:linear-gradient(120deg,#6e6a66 0%,#8c8884 40%,#57504b 75%,#3b3530 100%)}
.hero-cut{left:0;top:640px;width:1200px;height:130px}
.brand{display:flex;align-items:center;gap:10px;color:var(--white);font-weight:300;letter-spacing:0.5px}
.brand-dot{width:30px;height:30px;border-radius:50%;background:var(--orange)}
.site-brand{left:95px;top:22px;font-size:50px}
.nav{right:50px;top:42px;display:flex;gap:28px;font-size:15px;color:var(--white)}
.hero-brand{left:0;width:1200px;top:270px;justify-content:center;font-size:64px}
.hero-brand .brand-dot{width:40px;height:40px}
.hero-tagline{left:0;width:1200px;top:356px;text-align:center;color:var(--white);font-size:36px;font-weight:500;line-height:52px}
.side-nav{top:322px;width:20px;text-align:center;color:var(--white);font-size:14px;font-weight:600;line-height:40px}
.side-prev{left:45px}.side-next{left:1138px}
.slider-dots{left:568px;top:658px;display:flex;gap:12px}
.slider-dots span{width:9px;height:9px;border-radius:50%;background:var(--white)}

/* about */
.about-photo{left:600px;top:840px;width:515px;height:440px;background:linear-gradient(135deg,#c9ccd0,#7c8590 55%,#3a4350)}
.about-frame{left:618px;top:855px;width:462px;height:410px;border:3px solid var(--orange)}
.about-card{left:90px;top:880px;width:560px;height:360px;background:var(--white);box-shadow:0 2px 12px rgba(0,0,0,0.18);padding:36px 48px}
.section-title{font-size:36px;font-weight:700;color:var(--ink);text-transform:uppercase;letter-spacing:0.5px}
.section-title .first{color:var(--orange)}
.about-text{margin-top:14px;font-size:15px;line-height:30px;color:var(--ink)}
.btn{display:inline-block;margin-top:14px;background:var(--orange);color:var(--white);font-size:15px;padding:10px 26px;border-radius:22px;box-shadow:0 3px 6px rgba(0,0,0,0.2)}

/* services */
.services{left:0;top:1360px;width:1200px;height:578px;background:linear-gradient(180deg,#2d241e,var(--dark))}
.services .section-title{color:var(--white);text-align:center;margin-top:72px}
.services-lead{text-align:center;color:#e8e2dc;font-size:16px;line-height:30px;margin-top:12px}
.service-card{top:1593px;width:340px;height:268px}
.service-photo{width:100%;height:100%}
.service-card.active .service-overlay{position:absolute;inset:0;background:rgba(247,143,32,0.85);display:flex;align-items:center;justify-content:center;text-align:center;color:var(--white);font-size:21px;font-weight:600;line-height:38px;text-transform:uppercase}
.card-arrow{position:absolute;right:0;bottom:0;width:44px;height:38px;background:#1a1a1a}
.carousel-arrow{top:1712px}

/* blog */
.blog-title{left:0;width:1200px;top:2005px;text-align:center}
.post{top:2088px;width:352px;height:388px;background:var(--white);box-shadow:0 1px 10px rgba(0,0,0,0.16)}
.post-image{height:182px}
.post-body{padding:18px 22px 0}
.post-title{color:var(--orange);font-size:19px;font-weight:600;text-transform:uppercase}
.post-text{margin-top:6px;font-size:14.5px;line-height:25px;color:var(--ink)}
.post-meta{position:absolute;left:0;right:0;bottom:0;height:54px;border-top:1px solid #e4e4e4;padding:0 22px;display:flex;align-items:center;justify-content:space-between;font-size:11.5px;color:var(--orange)}
.comment-badge{width:34px;height:34px;border-radius:50%;background:var(--orange);display:flex;align-items:center;justify-content:center}
.blog-dots{left:570px;top:2518px;display:flex;gap:6px}
.blog-dots span{width:16px;height:16px;border-radius:50%;background:var(--orange)}
.blog-dots span.hollow{background:transparent;border:2px solid var(--orange)}

/* footer */
.footer{left:0;top:2615px;width:1200px;height:355px;background:var(--footer)}
.footer-brand{left:100px;top:2672px;font-size:46px}
.footer-about{left:100px;top:2745px;width:300px;font-size:12px;line-height:25px;color:#dddddd}
.footer-heading{font-size:19px;font-weight:700;color:var(--white);text-transform:uppercase}
.contact{left:530px;top:2670px}
.contact ul{list-style:none;margin-top:18px;font-size:12px;font-weight:600;color:var(--white);line-height:30px}
.newsletter{left:872px;top:2670px}
.newsletter-label{margin-top:14px;font-size:11px;color:var(--white);font-weight:500}
.signup{display:flex;margin-top:14px}
.signup-field{width:186px;height:32px;border:1px solid #cfcfcf;color:var(--white);font-size:11px;padding:8px 6px}
.signup-go{width:40px;height:32px;background:var(--orange);color:var(--white);font-size:15px;text-align:center;line-height:32px}
.social{display:flex;gap:8px;margin-top:12px}
.social span{width:12px;height:12px;background:var(--white)}
.footer-rule{left:78px;top:2870px;width:1044px;height:1px;background:#444}
.footer-nav{left:0;width:1200px;top:2888px;display:flex;justify-content:center;gap:20px;font-size:12px;color:var(--white)}
.copyright{left:0;width:1200px;top:2924px;text-align:center;font-size:12px;color:#dddddd}
</style>
</head>
<body>

<div class="abs hero" role="img" aria-label="Photo of a couple meeting a consultant across an office table"></div>
<svg class="abs hero-cut" width="1200" height="130" viewBox="0 0 1200 130"><polygon points="0,122 1200,20 1200,130 0,130" fill="#ffffff"/></svg>

<div class="abs brand site-brand"><span class="brand-dot"></span>brieflantern</div>
<nav class="abs nav"><span>Home</span><span>About US</span><span>Services</span><span>Blog</span><span>Contact</span></nav>

<div class="abs side-nav side-prev">P<br>R<br>E<br>V</div>
<div class="abs side-nav side-next">N<br>E<br>X<br>T</div>

<div class="abs brand hero-brand"><span class="brand-dot"></span>brieflantern</div>
<p class="abs hero-tagline">Don't Just Review<br>Investigate &amp; Discover</p>
<div class="abs slider-dots"><span></span><span></span><span></span><span></span></div>

<div class="abs about-photo" role="img" aria-label="Photo of two businessmen talking at a desk with a monitor"></div>
<div class="abs about-frame"></div>
<section class="abs about-card">
  <h2 class="section-title"><span class="first">A</span>bout Us</h2>
  <p class="about-text">I believe that proper application of technology can make or break the discovery process of small and large matters alike. Document review projects can create endless headaches without proper strategy and it is my goal to analyze every project individually and apply the proper level of technology to fit the client's needs.</p>
  <span class="btn">Read More</span>
</section>

<section class="abs services">
  <h2 class="section-title"><span class="first">O</span>ur Services</h2>
  <p class="services-lead">Sed ut perspiciatis unde omnis iste natus error sit voluptatem<br>accusantium doloremque laudantium</p>
</section>
<svg class="abs carousel-arrow" style="left:28px" width="48" height="24" viewBox="0 0 48 24"><path d="M46 12H4M14 2L4 12l10 10" stroke="#fff" stroke-width="3" fill="none"/></svg>
<svg class="abs carousel-arrow" style="left:1124px" width="48" height="24" viewBox="0 0 48 24"><path d="M2 12h42M34 2l10 10-10 10" stroke="#fff" stroke-width="3" fill="none"/></svg>

<div class="abs service-card" style="left:88px">
  <div class="service-photo" role="img" aria-label="Photo of two colleagues working at a laptop" style="background:linear-gradient(135deg,#dfe3e8,#8a97a8 60%,#3d4a60)"></div>
  <span class="card-arrow"><svg width="44" height="38" viewBox="0 0 44 38"><path d="M19 12l7 7-7 7" stroke="#fff" stroke-width="2.5" fill="none"/></svg></span>
</div>
<div class="abs service-card active" style="left:430px">
  <div class="service-photo" role="img" aria-label="Photo of a legal team meeting at a table" style="background:linear-gradient(135deg,#8a7a6a,#4c4038)"></div>
  <div class="service-overlay">Managed Litigation<br>Support</div>
  <span class="card-arrow"><svg width="44" height="38" viewBox="0 0 44 38"><path d="M19 12l7 7-7 7" stroke="#fff" stroke-width="2.5" fill="none"/></svg></span>
</div>
<div class="abs service-card" style="left:774px">
  <div class="service-photo" role="img" aria-label="Photo of two colleagues reviewing a tablet" style="background:linear-gradient(135deg,#e8eaec,#a3abb5 55%,#39404c)"></div>
  <span class="card-arrow"><svg width="44" height="38" viewBox="0 0 44 38"><path d="M19 12l7 7-7 7" stroke="#fff" stroke-width="2.5" fill="none"/></svg></span>
</div>

<h2 class="abs section-title blog-title"><span class="first">O</span>ur Blog</h2>

<article class="abs post" style="left:50px">
  <div class="post-image" role="img" aria-label="Review software product graphic" style="background:linear-gradient(135deg,#f2f2f4,#d9d9e2)"></div>
  <div class="post-body">
    <h3 class="post-title">Identifying Key Facts</h3>
    <p class="post-text">Imagine putting together a review process with a limited budget, expectations of a sizable yet manageable amount of data</p>
  </div>
  <div class="post-meta"><span>June 26, 2017 | Dana Whitlow</span><span class="comment-badge"><svg width="16" height="14" viewBox="0 0 16 14"><path d="M2 1h12v8H6l-3 3V9H2z" fill="#fff"/></svg></span></div>
</article>
<article class="abs post" style="left:425px">
  <div class="post-image" role="img" aria-label="Photo of a laptop and coffee on a desk" style="background:linear-gradient(135deg,#f0ede8,#c8c2b8 60%,#6d6560)"></div>
  <div class="post-body">
    <h3 class="post-title">Never Stop Discovering</h3>
    <p class="post-text">Learned knowledge and lessons learned are the absolute most important keys to success in any plaintiff review project</p>
  </div>
  <div class="post-meta"><span>December 29, 2016</span><span class="comment-badge"><svg width="16" height="14" viewBox="0 0 16 14"><path d="M2 1h12v8H6l-3 3V9H2z" fill="#fff"/></svg></span></div>
</article>
<article class="abs post" style="left:800px">
  <div class="post-image" role="img" aria-label="Photo of a team working over papers on a table" style="background:linear-gradient(135deg,#8c7256,#5a4634 60%,#3a2d22)"></div>
  <div class="post-body">
    <h3 class="post-title">The Natives Are Restless</h3>
    <p class="post-text">What is the definition of "Reasonably Usable" as it pertains to ESI and Document Review? &nbsp;Ask that question</p>
  </div>
  <div class="post-meta"><span>October 20, 2016 | Dana Whitlow</span><span class="comment-badge"><svg width="16" height="14" viewBox="0 0 16 14"><path d="M2 1h12v8H6l-3 3V9H2z" fill="#fff"/></svg></span></div>
</article>
<div class="abs blog-dots"><span class="hollow"></span><span></span><span></span></div>

<footer class="abs footer" role="img" aria-label="Dark photo backdrop of a person at work"></footer>
<div class="abs brand footer-brand"><span class="brand-dot"></span>brieflantern</div>
<p class="abs footer-about">Sed ut perspiciatis unde omnis iste natus error sit voluptatem accusantium doloremque laudantium, totam rem aperiam.</p>
<div class="abs contact">
  <h4 class="footer-heading">Get In Touch</h4>
  <ul>
    <li>PHONE : +1 123 456 7890</li>
    <li>FAX : +1 123 456 7890</li>
    <li>EMAIL: info@brieflantern-hub.com</li>
    <li>ADDRESS: 144 FF Designer Street</li>
  </ul>
</div>
<div class="abs newsletter">
  <h4 class="footer-heading">Newsletter</h4>
  <p class="newsletter-label">SIGN UP YOUR NEWSLETTER</p>
  <div class="signup"><span class="signup-field">EMAIL ADDRESS</span><span class="signup-go">GO</span></div>
  <div class="social"><span></span><span></span><span></span></div>
</div>
<div class="abs footer-rule"></div>
<nav class="abs footer-nav"><span>Home</span><span>|</span><span>About us</span><span>|</span><span>Services</span><span>|</span><span>Blog</span><span>|</span><span>Contact</span></nav>
<p class="abs copyright">Copyright © 2018 brieflantern. All rights reserved.</p>

</body>
</html>
```